Store Fixtures Company Business Card Design

We are looking for a business card design for a store fixture company. "Bright Shelf Outfitters" we help small businesses with their start up by providing fixtures required to display their products.
It should have a simple yet innovative design in the front, and a couple of sketch design for some sample products we carry in the back, to give a refined look to our company.
We would like our logo, do have one of our products "display cases" integrated in the design. And the rest of it just a clean look, which gives our address, store hours, and contact number, etc.
The color scheme as seen in the samples can be changed as long as the goal is achieved. The design attached just doesn't give off the direction we are looking to go.
Any off the attached products can be used as sketches in the back design. We do not want any name in the front.
Industry/Entity Type
Business
Contact Information for Business Card
Details shown in current business card design.

```html
<!DOCTYPE html>
<html lang="en">
<head>
<meta charset="utf-8">
<title>Bright Shelf Outfitters – Business Card</title>
<link rel="stylesheet" href="https://fonts.googleapis.com/css2?family=Open+Sans:wght@400;600;700;800&display=swap">
<style>
  :root {
    --backdrop: #3a3532;
    --card-dark: #0b0b0b;
    --card-light: #fbfbfb;
    --ink-light: #ededed;
    --ink-muted: #8d8d8d;
    --ink-dark: #1a1a1a;
    --ink-tagline-dark: #555555;
    --ghost: #1c1c1c;
    --case-top: #e4e9ec;
    --case-bottom: #aeb6bc;
  }
  html, body {
    margin: 0;
    width: 1200px;
    height: 900px;
    overflow: hidden;
    background: var(--backdrop);
    font-family: "Open Sans", Arial, sans-serif;
  }
  .canvas {
    position: relative;
    width: 1200px;
    height: 900px;
  }
  .card {
    position: absolute;
    top: 290px;
    width: 530px;
    height: 310px;
    box-shadow: 0 14px 30px rgba(0,0,0,.45);
    overflow: hidden;
  }
  .card--front { left: 50px; background: var(--card-dark); color: var(--ink-light); }
  .card--back  { left: 620px; background: var(--card-light); color: var(--ink-dark); }

  .ghost-ring {
    position: absolute;
    left: 250px;
    top: 30px;
    width: 230px;
    height: 230px;
    border-radius: 50%;
    border: 16px solid var(--ghost);
  }

  .brand {
    position: absolute;
    display: flex;
    align-items: center;
    gap: 12px;
  }
  .brand__dot {
    flex: none;
    width: 52px;
    height: 52px;
    border-radius: 50%;
    background: var(--ink-muted);
  }
  .brand__name {
    margin: 0;
    font-size: 18px;
    font-weight: 800;
    line-height: 1.1;
    letter-spacing: .2px;
    white-space: nowrap;
  }
  .brand__tagline {
    margin: 4px 0 0;
    font-size: 6.5px;
    font-weight: 700;
    letter-spacing: 1.6px;
    text-transform: uppercase;
    white-space: nowrap;
  }
  .card--front .brand { left: 34px; top: 40px; }
  .card--front .brand__name { color: var(--ink-light); }
  .card--front .brand__tagline { color: var(--ink-muted); }

  .hours {
    position: absolute;
    left: 34px;
    top: 182px;
    margin: 0;
    font-size: 15px;
    line-height: 1.35;
    color: var(--ink-muted);
  }
  .hours strong { font-weight: 600; }
  .address {
    position: absolute;
    left: 34px;
    top: 238px;
    margin: 0;
    font-style: normal;
    font-size: 17px;
    line-height: 1.3;
  }
  .address__street { color: var(--ink-muted); font-weight: 600; }
  .address__city { color: var(--ink-light); }

  .contact {
    position: absolute;
    left: 300px;
    top: 150px;
    margin: 0;
    padding: 0;
    list-style: none;
    font-size: 14px;
    line-height: 1.5;
  }
  .contact li { display: flex; align-items: center; gap: 7px; }
  .contact svg { width: 11px; height: 11px; fill: var(--ink-muted); }

  .display-case {
    position: absolute;
    left: 48px;
    top: 40px;
    width: 170px;
    height: 230px;
    background: linear-gradient(160deg, var(--case-top), var(--case-bottom));
  }
  .card--back .brand { left: 240px; top: 112px; }
  .card--back .brand__dot { background: var(--ink-dark); width: 46px; height: 46px; }
  .card--back .brand__name { color: var(--ink-dark); }
  .card--back .brand__tagline { color: var(--ink-tagline-dark); }
</style>
</head>
<body>
<main class="canvas">
  <section class="card card--front" aria-label="Card front">
    <div class="ghost-ring" aria-hidden="true"></div>
    <div class="brand">
      <span class="brand__dot" aria-hidden="true"></span>
      <div>
        <p class="brand__name">Bright Shelf Outfitters</p>
        <p class="brand__tagline">Display better, sell more</p>
      </div>
    </div>

    <p class="hours"><strong>Mon-Fri:</strong> 9am-5.30pm<br><strong>Sat:</strong> 11am-3pm</p>
    <address class="address">
      <span class="address__street">4180 Larkspur Drive</span><br>
      <span class="address__city">Houston, TX 77099</span>
    </address>

    <ul class="contact">
      <li>
        <svg viewBox="0 0 12 12" aria-hidden="true"><path d="M1 2.5C1 1.7 1.7 1 2.5 1h1.2l1 2.6-1.2.9a6 6 0 0 0 4 4l.9-1.2 2.6 1v1.2c0 .8-.7 1.5-1.5 1.5C5 11 1 7 1 2.5z"/></svg>
        713.555.0142
      </li>
      <li>
        <svg viewBox="0 0 12 12" aria-hidden="true"><rect x="3" y="1" width="6" height="3"/><rect x="1" y="4.5" width="10" height="4.5" rx="1"/><rect x="3" y="8" width="6" height="3"/></svg>
        713.555.0187
      </li>
      <li>
        <svg viewBox="0 0 12 12" aria-hidden="true"><circle cx="6" cy="6" r="5"/></svg>
        www.brightshelfco.com
      </li>
    </ul>
  </section>

  <section class="card card--back" aria-label="Card back">
    <div class="display-case" role="img" aria-label="Illustration of a glass display case with shelves"></div>
    <div class="brand">
      <span class="brand__dot" aria-hidden="true"></span>
      <div>
        <p class="brand__name">Bright Shelf Outfitters</p>
        <p class="brand__tagline">Display better, sell more</p>
      </div>
    </div>
  </section>
</main>
</body>
</html>
```